Bed & Breakfast PressBlog Theme - Design Only

We are looking for a PressBlog theme for an award winning UK Bed & Breakfast (Guesthouse) www.fernbrookinn.co.uk
You will see that the current site is basic and dated, we need a new site that showcases the very high standard of rooms on offer and is geared towards both mobile and desktop browsing.
We would like the colours that have been used in the rooms and building (as seen on the current website) to feature in the design.
We particularly like the look of this accommodation provider website: http://www.marlowdenbarns.co.uk
Selected website images can be downloaded here, feel free to use more from the existing website too:
https://www.filevaultly.com/s/qz81mv4rt7kw0pn/website%20images.zip
Target Market(s)
The accommodation is upmarket and the design needs to subtly communicate this.
The accommodation attracts a varied mix of ages so needs to be up scale without being overly modern.
Industry/Entity Type
Accommodation
Requirements
Must have
- As the accommodation does not have a logo we need a basic typographic logo incorporated into the design.
Colours of the building and rooms must be integrated into the design in some way.
A bold homepage that allows images of the rooms on offer and key information to be visibale above the fold. The goal of the homepage is for someone to then click Rooms or Prices so calls to action may help here.
Separate designs for a sidebar and full width version of sub pages.
An area that shows off the awards won by the company on all pages and space for testimonials.
The site must enable an easy transition from - homepage - to rooms - to prices with possible call to action buttons in the top right corner on these pages
The site needs to have a Homepage layout, a general sub page layout, and a 'Rooms' page layout which will showcase all rooms available possibly in a grid layout.
Nice to have
- Please use some of the images available currently on the website in your mockup, particularly of the building and rooms.
Should not have
- No need for any type of booking fields or engine as the booking system will be embedded on a full width page.

```html
<!DOCTYPE html>
<html lang="en">
<head>
<meta charset="utf-8">
<title>Fernbrook Inn – A small and friendly hotel</title>
<link rel="stylesheet" href="https://fonts.googleapis.com/css2?family=Roboto+Condensed:ital,wght@0,400;0,700;1,400;1,700&family=Open+Sans:ital,wght@0,400;0,600;0,700;1,400;1,600&display=swap">
<style>
:root{
  --green:#4fae3c;
  --green-dark:#2f8a23;
  --green-light:#6cc753;
  --ink:#1f1f1f;
  --text:#3a3a3a;
  --muted:#6b6b6b;
  --header:#262626;
  --footer:#2b2b2b;
  --footer-bar:#1e1e1e;
  --beige:#efe6d2;
  --panel:#ffffff;
  --tab:#e3e3e3;
  --line:#c9c9c9;
  --gold:#e8b94a;
  --purple:#7b3d98;
}
*{box-sizing:border-box;margin:0;padding:0}
html,body{width:1200px;height:2476px;overflow:hidden}
body{
  position:relative;
  background:linear-gradient(var(--header) 0,var(--header) 380px,var(--beige) 380px);
  font-family:"Open Sans",Arial,sans-serif;
  color:var(--text);
  font-size:13px;
}
a{color:inherit;text-decoration:none}
.abs{position:absolute}

/* header */
.brand{left:82px;top:20px;width:400px;height:128px;
  background:linear-gradient(#f7f7f7,#d9d9d9);
  clip-path:polygon(0 8%,2% 0,88% 0,100% 100%,0 100%);
  border-radius:10px 0 0 0;padding:22px 0 0 22px}
.brand-name{font-family:"Roboto Condensed",Arial,sans-serif;font-weight:700;font-size:50px;color:var(--green);line-height:1}
.brand-tag{font-family:"Open Sans",Arial,sans-serif;font-weight:700;font-size:15px;letter-spacing:1.6px;color:#4a4a4a;margin-top:10px;padding-left:6px}
.top-address{right:86px;top:24px;font-style:italic;color:#9a9a9a;font-size:14.5px}
.top-contact{right:86px;top:58px;display:flex;gap:28px;color:#fff;font-weight:600;font-size:16px}
.top-contact span{display:flex;align-items:center;gap:8px}
.cta{left:660px;top:106px;display:flex;height:42px}
.cta a{display:flex;align-items:center;justify-content:center;color:#14340f;font-family:"Roboto Condensed",Arial,sans-serif;font-weight:700;font-size:21px;
  background:linear-gradient(var(--green-light),var(--green));border-radius:14px 0 0 0;width:156px}
.cta a+a{background:linear-gradient(#5dbb47,var(--green-dark));color:#fff;border-radius:0 14px 0 0;width:136px}
.cta a:first-child{color:#fff}
.hero{left:82px;top:148px;width:1036px;height:438px;
  background:radial-gradient(ellipse at 55% 70%,#fbf6ec 0,#e9dcc5 30%,#b88f64 62%,#6b4b33 100%)}

/* nav */
.main-nav{left:82px;top:586px;width:1036px;height:51px;display:flex;gap:2px;background:#fff}
.main-nav a{flex:1 1 auto;display:flex;align-items:center;justify-content:center;
  background:linear-gradient(#f0f0f0,#d8d8d8);font-family:"Roboto Condensed",Arial,sans-serif;font-weight:700;font-size:21px;color:#7b7b7b}
.main-nav a.is-active{background:linear-gradient(var(--green-light),var(--green-dark));color:#fff}

/* panel */
.panel{left:82px;top:637px;width:1036px;height:1541px;background:var(--panel)}
.col{left:102px;width:662px}
h2.section{font-family:"Roboto Condensed",Arial,sans-serif;font-weight:400;font-size:21px;color:var(--ink)}
.welcome{top:664px}
.welcome p{margin-top:10px;line-height:1.5}
.welcome .lead{font-size:14.5px;color:var(--ink);margin-top:14px}
.welcome .lead a{color:var(--green-dark);font-style:italic}
.dash{left:102px;width:662px;border-top:2px dashed #cfcfcf}
.photo{background:linear-gradient(135deg,#e9e4da,#a9a08f)}
.photo.house{left:102px;top:932px;width:302px;height:149px;background:linear-gradient(160deg,#d9e6c7 0,#f2f2ef 40%,#6d8a4c 100%)}
.photo.dining{left:102px;top:1091px;width:302px;height:148px;background:linear-gradient(150deg,#7b4a3e 0,#cfc8be 45%,#5a4036 100%)}
.about{left:424px;top:930px;width:340px;font-style:italic;color:#5a5a5a;font-size:12.3px;line-height:1.45}
.about p{margin-bottom:8px}
.about .about-title{color:var(--ink);font-weight:600;font-size:12.8px}
.offers{left:102px;top:1304px;width:662px;height:76px;display:flex;background:#2f2f2f}
.offers-label{width:168px;background:linear-gradient(#f0c85c,var(--gold));clip-path:polygon(0 0,86% 0,100% 50%,86% 100%,0 100%);
  font-family:"Roboto Condensed",Arial,sans-serif;font-style:italic;font-size:21px;color:#2a2a2a;padding:14px 0 0 22px;line-height:1.1}
.offers-quote{flex:1;font-family:"Roboto Condensed",Arial,sans-serif;font-style:italic;color:#a8a8a8;font-size:17px;padding:14px 0 0 26px;line-height:1.35}
.offers-book{width:78px;background:linear-gradient(var(--green-light),var(--green-dark));color:#fff;font-family:"Roboto Condensed",Arial,sans-serif;font-weight:700;font-size:19px;text-align:center;padding-top:12px;line-height:1.15;
  clip-path:polygon(12% 0,100% 0,100% 100%,0 100%,12% 50%,0 0)}
.rooms-title{top:1436px}
.room-grid{left:102px;top:1482px;width:662px;display:grid;grid-template-columns:repeat(3,208px);gap:21px 19px}
.room{height:157px;background:#fff;box-shadow:0 3px 4px rgba(0,0,0,.18)}
.room-label{height:31px;background:linear-gradient(#e6e6e6,#cfcfcf);font-size:14.5px;color:#333;padding:6px 0 0 12px}
.room.is-featured .room-label{background:linear-gradient(var(--green-light),var(--green-dark));color:#fff}
.room-photo{height:126px;background:linear-gradient(150deg,#f4ede2,#b9946a 70%,#6a4a30);display:flex;align-items:center;justify-content:center;gap:10px}
.room.is-featured .room-photo{background:linear-gradient(#4a4a4a,#2a2a2a)}
.room.is-dark .room-photo{background:linear-gradient(150deg,#8a6a4a,#d8c6a6 55%,#3d2c20)}
.round-btn{width:34px;height:34px;border-radius:50%;display:flex;align-items:center;justify-content:center}
.awards-title{left:120px;top:2020px;font-family:"Roboto Condensed",Arial,sans-serif;font-size:24px;color:var(--green-dark)}
.awards{left:102px;top:2046px;width:664px;height:102px;border:2px solid #ddd;border-radius:10px;display:flex;align-items:center;justify-content:space-between;padding:0 12px}
.award-arrow{width:30px;height:30px;border-radius:50%;background:#fff;box-shadow:0 1px 4px rgba(0,0,0,.3);display:flex;align-items:center;justify-content:center}
.award-row{display:flex;gap:52px;flex:1;justify-content:center}
.badge{width:74px;height:74px;border-radius:50%}

/* sidebar */
.side{left:787px;width:309px}
.side-head{height:40px;background:linear-gradient(var(--green-light),var(--green-dark));color:#fff;font-family:"Roboto Condensed",Arial,sans-serif;font-size:21px;padding:6px 0 0 16px;border-radius:6px 6px 0 0}
.services{top:665px;box-shadow:0 2px 6px rgba(0,0,0,.2)}
.services ul{list-style:none}
.services li{height:41.5px;border-top:1px solid #ddd;background:#f4f4f4;display:flex;align-items:center;gap:12px;padding-left:12px;font-size:14.5px;color:#555}
.services li.is-current{background:#e6e6e6;color:#111}
.services svg{width:22px;height:18px;fill:#6f6f6f}
.video{top:1061px;height:234px;background:linear-gradient(#1e1e1e,#3b3630 60%,#1a1a1a);position:absolute}
.video-caption{position:absolute;left:34px;top:20px;width:250px;color:#c9c9c9;font-style:italic;font-size:13.5px;line-height:1.4}
.video-play{position:absolute;left:130px;top:94px;width:50px;height:50px;border-radius:50%;background:rgba(0,0,0,.55);border:2px solid #ddd;display:flex;align-items:center;justify-content:center}
.video-bar{position:absolute;left:0;bottom:0;width:100%;height:20px;background:#111;display:flex;align-items:center;padding:0 10px;gap:10px}
.video-track{flex:1;height:4px;background:#555}
.video-track i{display:block;width:30%;height:4px;background:#c33}
.direct{top:1317px;height:326px;background:linear-gradient(#8a4aa6,var(--purple));text-align:center;padding-top:16px}
.direct-badge{width:150px;height:150px;margin:0 auto;border:5px solid #fff;border-radius:10px;background:#9a5bb4}
.direct-line{font-family:"Roboto Condensed",Arial,sans-serif;font-weight:700;color:#fff;font-size:44px;line-height:1.02;margin-top:14px}
.direct-btn{display:inline-block;margin-top:12px;background:linear-gradient(#9bcf5a,#6aa634);color:#fff;font-weight:700;font-size:13px;padding:6px 18px;border-radius:6px}
.certs{top:1648px;height:90px;display:flex;justify-content:space-between}
.cert{width:112px;text-align:center;font-size:11px;color:#2a5d9a;text-decoration:underline}
.cert i{display:block;height:66px;border:2px solid #ccc;background:#f2f2f2;margin-bottom:4px}
.cert.wide{width:172px;font-weight:700;color:#222}
.cert.wide i{background:linear-gradient(var(--green-light),var(--green-dark));border:none;border-radius:8px 8px 0 0}
.newsletter{top:1759px;height:96px;background:#f0f0f0;border:1px solid #ddd;padding:12px 14px}
.newsletter h3{font-family:"Roboto Condensed",Arial,sans-serif;font-weight:700;font-size:21px;color:#222}
.newsletter form{display:flex;margin-top:14px;width:210px}
.newsletter input{flex:1;height:22px;border:none;background:#cfcfcf;font-size:11px;padding-left:8px;font-family:inherit}
.newsletter button{width:26px;border:none;background:#999;color:#fff;font-size:11px}
.mail-seal{position:absolute;right:-2px;top:26px}
.testimonials{top:1878px;height:270px;border:1px solid #ddd;box-shadow:0 2px 4px rgba(0,0,0,.12)}
.testimonials .side-head{border-radius:4px 4px 0 0}
.quote-head{display:flex;gap:16px;padding:16px 16px 0}
.avatar{width:76px;height:76px;border-radius:50%;background:linear-gradient(#8fa7c2,#3d4c5a)}
.quote-name{color:#2a8bd0;font-size:15px;font-weight:600;margin-top:8px}
.quote-role{font-size:12px;color:#444}
.quote-date{font-style:italic;font-size:11px;color:#444;margin-top:3px}
.quote-body{padding:12px 16px;font-size:12.5px;color:#777;line-height:1.45}
.quote-nav{position:absolute;bottom:0;left:0;width:100%;display:flex;justify-content:space-between}
.quote-nav span{width:22px;height:22px;background:#ccc;display:flex;align-items:center;justify-content:center}
.quote-nav span+span{background:var(--green)}

/* footer */
.site-footer{left:0;top:2178px;width:1200px;height:244px;background:var(--footer)}
.foot-col{top:2198px}
.foot-col h4{font-family:"Roboto Condensed",Arial,sans-serif;font-weight:400;font-size:18px;color:var(--green)}
.foot-col ul{list-style:none;margin-top:12px}
.foot-menu li{font-size:13px;color:#8a8a8a;line-height:24.5px}
.foot-menu li.is-current{color:#fff}
.foot-social li{display:flex;align-items:center;gap:8px;font-size:13px;color:#8a8a8a;height:37px}
.foot-social i{width:24px;height:24px;background:#5a5a5a}
.foot-contact li{display:flex;gap:14px;font-size:13px;color:#9a9a9a;line-height:1.55;margin-bottom:22px}
.foot-contact li.mail{font-style:italic}
.map{left:835px;top:2222px;width:279px;height:114px;border:3px solid #ddd;background:linear-gradient(135deg,#e9ecef,#cfd8d0)}
.copyright{left:0;top:2422px;width:1200px;height:54px;background:var(--footer-bar);color:#6f6f6f;font-size:12.5px;text-align:center;line-height:54px}
</style>
</head>
<body>

<header>
  <div class="abs brand">
    <div class="brand-name">Fernbrook Inn</div>
    <div class="brand-tag">A Small and friendly hotel</div>
  </div>
  <div class="abs top-address">Fernbrook Inn, Mill Lane, Ashcombe, Dorset DT9 4QR</div>
  <div class="abs top-contact">
    <span><svg width="18" height="18" viewBox="0 0 24 24"><path fill="#5fc24a" d="M6.6 10.8a15 15 0 0 0 6.6 6.6l2.2-2.2c.3-.3.7-.4 1-.2 1.1.4 2.3.6 3.6.6.6 0 1 .4 1 1V20c0 .6-.4 1-1 1A17 17 0 0 1 3 4c0-.6.4-1 1-1h3.5c.6 0 1 .4 1 1 0 1.3.2 2.5.6 3.6.1.3 0 .7-.2 1z"/></svg>01632 960418</span>
    <span><svg width="20" height="16" viewBox="0 0 24 18"><rect x="1" y="1" width="22" height="16" fill="#5fc24a"/><path d="M1 1l11 9 11-9" stroke="#262626" stroke-width="2" fill="none"/></svg>enquiries@fernbrookinn.co.uk</span>
  </div>
  <nav class="abs cta"><a href="#">Book Now</a><a href="#">Find Us</a></nav>
  <div class="abs hero" role="img" aria-label="Guest bedroom with a driftwood four-poster bed, white linen and bedside lamps"></div>
  <nav class="abs main-nav">
    <a class="is-active" href="#" style="max-width:117px">Home</a>
    <a href="#" style="max-width:134px">Rooms</a>
    <a href="#" style="max-width:122px">Prices</a>
    <a href="#" style="max-width:205px">Picture Gallery</a>
    <a href="#" style="max-width:170px">Information</a>
    <a href="#" style="max-width:149px">Sitemap</a>
    <a href="#" style="max-width:130px">Contact</a>
  </nav>
</header>

<main>
  <div class="abs panel"></div>

  <section class="abs col welcome">
    <h2 class="section">Welcome to Fernbrook Inn</h2>
    <p class="lead">Fernbrook Inn is a: 'small and friendly hotel'.</p>
    <p style="margin-top:6px">Award-Winning, Eco Chic, Environmentally-Responsible, New Forest Accommodation offering 24 hour front desk, daily housekeeping, private bathroom for every room.</p>
    <p class="lead">Why not book dinner at <a href="#">www.oakhollowkitchen.co.uk</a> at the Fernbrook Inn</p>
    <p style="margin-top:6px">News : Coming down by train? Want to get about whilst you are in the New Forest? Rent a Zippa for just £20 per half hour. What's a Zippa?</p>
    <p style="margin-top:6px">Its a two person electric car.</p>
  </section>
  <div class="abs dash" style="top:900px"></div>

  <div class="abs photo house" role="img" aria-label="White-painted inn exterior with yellow front door and garden"></div>
  <div class="abs photo dining" role="img" aria-label="Breakfast room table laid with glassware"></div>
  <section class="abs about">
    <p class="about-title">About 17th century new forest accommodation: New Forest Hotel.</p>
    <p>Rating: RTA 2 star small and friendly hotel - Formerly Best New Forest B&amp;B in SE England more...</p>
    <p>Eating: 12 lovely eateries 10 mins walk more...</p>
    <p>Near Ridgefield, Hartley's Manor, Elmstead Lawn...</p>
    <p>New Forest walks, cycling, horse riding, more...</p>
    <p>Dogs and families: children welcome more...</p>
    <p>Special Needs: more...</p>
    <p>Romance: Four Poster, New Forest Weddings, more...</p>
    <p>Business: Free WIFI, room only prices, more...</p>
    <p>Image Gallery | Sitemap</p>
  </section>
  <div class="abs dash" style="top:1271px"></div>

  <aside class="abs offers">
    <div class="offers-label">Our Special<br>Offers</div>
    <div class="offers-quote">"December 2013 - Small and friendly hotel.<br>Formerly RTA's highest rated New Forest B&amp;B 2013"</div>
    <a class="offers-book" href="#">Book<br>Now</a>
  </aside>
  <div class="abs dash" style="top:1411px"></div>

  <h2 class="abs col section rooms-title" style="font-size:24px">Our Rooms</h2>
  <section class="abs room-grid">
    <a class="room is-featured" href="#"><div class="room-label">Browse all Rooms</div>
      <div class="room-photo" role="img" aria-label="Bedroom preview">
        <span class="round-btn" style="background:var(--green)"><svg width="16" height="16" viewBox="0 0 24 24"><path d="M10 14l4-4M8 12l-3 3a3 3 0 0 0 4 4l3-3M16 12l3-3a3 3 0 0 0-4-4l-3 3" stroke="#fff" stroke-width="2.4" fill="none"/></svg></span>
        <span class="round-btn" style="background:#fff"><svg width="16" height="16" viewBox="0 0 24 24"><circle cx="10" cy="10" r="6" stroke="#333" stroke-width="2.4" fill="none"/><path d="M15 15l5 5" stroke="#333" stroke-width="2.6"/></svg></span>
      </div></a>
    <a class="room" href="#"><div class="room-label">Compare Rooms</div><div class="room-photo" role="img" aria-label="Bright bedroom with timber posts"></div></a>
    <a class="room" href="#"><div class="room-label">Floor Plan</div><div class="room-photo" role="img" aria-label="Wooden staircase up to a garden room" style="background:linear-gradient(#cfe0ef,#a06a3e 60%,#5b3b22)"></div></a>
    <a class="room is-dark" href="#"><div class="room-label">Small doubles / Singles</div><div class="room-photo" role="img" aria-label="Small double room"></div></a>
    <a class="room" href="#"><div class="room-label">Doubles</div><div class="room-photo" role="img" aria-label="Double room with wooden bed"></div></a>
    <a class="room is-dark" href="#"><div class="room-label">Twin</div><div class="room-photo" role="img" aria-label="Twin room"></div></a>
    <a class="room" href="#"><div class="room-label">Four Poster</div><div class="room-photo" role="img" aria-label="Four poster room" style="background:linear-gradient(150deg,#f2efe9,#6a4a3a 70%,#2f2018)"></div></a>
    <a class="room" href="#"><div class="room-label">Triples</div><div class="room-photo" role="img" aria-label="Triple room"></div></a>
    <a class="room is-dark" href="#"><div class="room-label">Dog friendly</div><div class="room-photo" role="img" aria-label="Dog friendly room"></div></a>
  </section>

  <h2 class="abs awards-title">Our Awards</h2>
  <section class="abs awards">
    <span class="award-arrow"><svg width="12" height="14" viewBox="0 0 12 14"><path d="M9 1L3 7l6 6" stroke="#333" stroke-width="2.6" fill="none"/></svg></span>
    <div class="award-row">
      <span class="badge" style="background:#1f2a6b"></span>
      <span class="badge" style="background:#2b3d8f"></span>
      <span class="badge" style="background:#e9a83a;border-radius:8px;width:60px"></span>
      <span class="badge" style="background:#4fb0c9;border-radius:50% 8px"></span>
      <span class="badge" style="background:#3d8a2b"></span>
    </div>
    <span class="award-arrow"><svg width="12" height="14" viewBox="0 0 12 14"><path d="M3 1l6 6-6 6" stroke="#333" stroke-width="2.6" fill="none"/></svg></span>
  </section>

  <!-- sidebar -->
  <section class="abs side services">
    <div class="side-head">Our Services</div>
    <ul>
      <li class="is-current"><svg viewBox="0 0 22 18"><rect x="1" y="1" width="20" height="12" fill="#222"/><rect x="7" y="14" width="8" height="3" fill="#222"/></svg>Book Online</li>
      <li><svg viewBox="0 0 22 18"><rect x="1" y="8" width="20" height="6"/><rect x="1" y="4" width="3" height="12"/><rect x="18" y="4" width="3" height="12"/></svg>Room Facilities</li>
      <li><svg viewBox="0 0 22 18"><path d="M2 2h9l9 9-7 7-9-9z"/></svg>Special Offers</li>
      <li><svg viewBox="0 0 22 18"><rect x="3" y="6" width="16" height="11"/><rect x="2" y="3" width="18" height="4"/></svg>Gift Vouchers</li>
      <li><svg viewBox="0 0 22 18"><path d="M6 1h10v5a5 5 0 0 1-10 0z"/><rect x="9" y="11" width="4" height="4"/><rect x="6" y="15" width="10" height="2"/></svg>Awards</li>
      <li><svg viewBox="0 0 22 18"><path d="M3 9l5 5L19 3" stroke="#6f6f6f" stroke-width="3" fill="none"/></svg>B&amp;B Accessibility</li>
      <li><svg viewBox="0 0 22 18"><circle cx="11" cy="7" r="6"/><rect x="10" y="11" width="2" height="7"/></svg>Our Environment</li>
      <li><svg viewBox="0 0 22 18"><rect x="2" y="6" width="18" height="7" rx="2"/><circle cx="6" cy="14" r="2.5"/><circle cx="16" cy="14" r="2.5"/></svg>Leave the Car at home</li>
    </ul>
  </section>

  <section class="abs side video" role="img" aria-label="Video preview of the inn breakfast table">
    <p class="video-caption">Fernbrook Inn New Forest Small and friendlyhotel. Formerly a 5 star B&amp;B</p>
    <span class="video-play"><svg width="18" height="20" viewBox="0 0 18 20"><path d="M2 1l15 9-15 9z" fill="#fff"/></svg></span>
    <div class="video-bar">
      <svg width="10" height="10" viewBox="0 0 10 10"><rect x="1" y="0" width="3" height="10" fill="#ddd"/><rect x="6" y="0" width="3" height="10" fill="#ddd"/></svg>
      <span class="video-track"><i></i></span>
      <span style="color:#aaa;font-size:9px">0:02 / 0:11</span>
    </div>
  </section>

  <aside class="abs side direct">
    <div class="direct-badge" role="img" aria-label="Book direct price promise badge"></div>
    <p class="direct-line">Best price<br>guaranteed!</p>
    <a class="direct-btn" href="#">Find out more</a>
  </aside>

  <div class="abs side certs">
    <a class="cert" href="#"><i role="img" aria-label="Certificate of excellence badge"></i>Fernbrook Inn</a>
    <a class="cert wide" href="#"><i role="img" aria-label="Recommended on TravelScore badge"></i>Fernbrook Inn</a>
  </div>

  <section class="abs side newsletter">
    <h3>Newsletter</h3>
    <form><input type="text" placeholder="E-mail" aria-label="E-mail"><button type="button">Go</button></form>
    <svg class="mail-seal" width="64" height="64" viewBox="0 0 64 64"><circle cx="32" cy="32" r="30" fill="#888"/><circle cx="32" cy="32" r="24" fill="#f0f0f0"/><rect x="20" y="24" width="24" height="17" fill="#777"/><path d="M20 24l12 10 12-10" stroke="#f0f0f0" stroke-width="2" fill="none"/></svg>
  </section>

  <section class="abs side testimonials">
    <div class="side-head">Testimonials</div>
    <div class="quote-head">
      <div class="avatar" role="img" aria-label="Guest portrait"></div>
      <div>
        <p class="quote-name">Dr.Lorem</p>
        <p class="quote-role">(amet ahet dymmy text)</p>
        <p class="quote-date">Posted on 25 Spet,2013</p>
      </div>
    </div>
    <p class="quote-body">Lorem ipsum dolor sit amet, conur adipiscing elit. Proin interdum lobtis libero id convallis. Nullam sit amet tinnt massa.Proin interdum loborti</p>
    <div class="quote-nav">
      <span><svg width="8" height="10" viewBox="0 0 8 10"><path d="M6 1L2 5l4 4" stroke="#fff" stroke-width="2" fill="none"/></svg></span>
      <span><svg width="8" height="10" viewBox="0 0 8 10"><path d="M2 1l4 4-4 4" stroke="#fff" stroke-width="2" fill="none"/></svg></span>
    </div>
  </section>
</main>

<footer>
  <div class="abs site-footer"></div>
  <nav class="abs foot-col" style="left:82px">
    <h4>Menu</h4>
    <ul class="foot-menu">
      <li class="is-current">Home</li><li>Rooms</li><li>Prices</li><li>Picture Gallery</li><li>Information</li><li>Sitemap</li><li>Contact</li>
    </ul>
  </nav>
  <div class="abs foot-col" style="left:332px">
    <h4>Follow Us</h4>
    <ul class="foot-social">
      <li><i></i>Friendbook</li><li><i></i>Chirper</li><li><i></i>Circles +</li><li><i></i>ViewTube</li><li><i></i>PressBlog</li>
    </ul>
  </div>
  <div class="abs foot-col" style="left:594px;width:230px">
    <h4>Contact Us</h4>
    <ul class="foot-contact">
      <li><svg width="16" height="22" viewBox="0 0 16 22"><path d="M8 1a7 7 0 0 1 7 7c0 5-7 13-7 13S1 13 1 8a7 7 0 0 1 7-7z" fill="#777"/><circle cx="8" cy="8" r="2.6" fill="#2b2b2b"/></svg><span>Fernbrook Inn, Mill Lane,<br>Ashcombe, Dorset<br>DT9 4QR</span></li>
      <li><svg width="16" height="16" viewBox="0 0 24 24"><path fill="#777" d="M6.6 10.8a15 15 0 0 0 6.6 6.6l2.2-2.2c.3-.3.7-.4 1-.2 1.1.4 2.3.6 3.6.6.6 0 1 .4 1 1V20c0 .6-.4 1-1 1A17 17 0 0 1 3 4c0-.6.4-1 1-1h3.5c.6 0 1 .4 1 1 0 1.3.2 2.5.6 3.6.1.3 0 .7-.2 1z"/></svg>01632 960418</li>
      <li class="mail"><svg width="18" height="14" viewBox="0 0 24 18"><rect x="1" y="1" width="22" height="16" fill="#777"/><path d="M1 1l11 9 11-9" stroke="#2b2b2b" stroke-width="2" fill="none"/></svg>enquiries@fernbrookinn.co.uk</li>
    </ul>
  </div>
  <div class="abs map" role="img" aria-label="Street map showing the inn's location"></div>
  <p class="abs copyright">Copyright © 2013 Fernbrook Inn. All rights reserved.</p>
</footer>

</body>
</html>
```